Mobile Recording Studio needs business cards

Open to seeing a creative design, but I want to emphasis my logo and minimize the name/title and company information. Possible a fully black background on card.

My company is a mobile sound recording studio. ok to include a my trailer (actual or cartoon) on the card. My initial thought is more straight forward, but a good design will win me over.

SPECS:
CMYK color mode
High (300ppi) raster effect.
cover bleed area
please deliver: Illustrator file with layers and a pdf at completion.

Name and info for the business card:

Dallin Perry
ADR Mixer

email: Dallin@MixVault.com

address:
248 - 5170 East Hollister
Vancouver, BC V5R 2J4

phone:
604.518.2093 office

website:
www.MixVault.com

FB: @MixVault

Instagram: @TheMixVault

Industry/Entity Type

Television Production

Contact Information for Business Card

Dallin Perry
ADR Mixer

email: Dallin@MixVault.com

address:
248 - 5170 East Hollister
Vancouver, BC V5R 2J4

phone:
604.518.2093 office

website:
www.MixVault.com

FB: @MixVault

Instagram: @TheMixVault

Colors

Designer to choose colors to be used in the design.

Requirements
Must have
• emphasis my logo and minimize the name/title and company information.
• SPECS:
• CMYK color mode
• High (300ppi) raster effect.
• cover bleed area
• please deliver: Illustrator file with layers and a pdf at completion.
Nice to have
• maybe include the following:
• all black background or black theme
• my work trailer (actual or cartoon) refer to Instagram: @TheMixVault

```html
<!DOCTYPE html>
<html lang="en">
<head>
<meta charset="UTF-8">
<title>MixVault Business Cards</title>
<link href="https://fonts.googleapis.com/css2?family=Montserrat:wght@400;500;600;700&display=swap" rel="stylesheet">
<style>
  :root {
    --canvas: #cccccc;
    --ink-black: #060708;
    --paper: #ffffff;
    --frame-dark: #d9d9d9;
    --frame-light: #dcdcdc;
    --silver: #cfcfcf;
    --text-dark: #1a1a1a;
    --text-muted: #8a8a8a;
    --icon: #8d8d8d;
  }
  * { box-sizing: border-box; margin: 0; padding: 0; }
  html, body {
    width: 1200px; height: 1000px; overflow: hidden;
    background: var(--canvas);
    font-family: "Montserrat", sans-serif;
  }
  .sheet { position: relative; width: 1200px; height: 1000px; }

  .card {
    position: absolute; width: 515px; height: 308px;
    box-shadow: 0 1px 2px rgba(0,0,0,0.12);
    overflow: hidden;
  }
  .card--front { left: 62px; background: var(--paper); }
  .card--back { left: 622px; background: radial-gradient(ellipse at 50% 60%, #111315 0%, var(--ink-black) 70%); }
  .row-1 { top: 170px; }
  .row-2 { top: 521px; }

  .card__band {
    position: absolute; left: 0; top: 0; width: 100%; height: 131px;
    background: linear-gradient(180deg, #060708 0%, #0b0d0e 100%);
  }
  .card__frame {
    position: absolute; left: 28px; top: 28px; width: 459px; height: 252px;
    border: 1px solid var(--frame-light);
  }
  .card--back .card__frame { border-color: var(--frame-dark); }

  .brand-small {
    position: absolute; left: 50px; top: 62px;
    font-size: 22px; font-weight: 600; color: var(--silver);
    letter-spacing: 0.5px;
  }
  .brand-large {
    position: absolute; left: 0; right: 0; top: 118px;
    text-align: center;
    font-size: 60px; font-weight: 600; color: var(--silver);
    letter-spacing: 1px; line-height: 1;
  }

  .person { position: absolute; left: 48px; top: 203px; }
  .person__name {
    font-size: 17px; font-weight: 700; color: var(--text-dark);
    letter-spacing: 0.3px; line-height: 22px;
  }
  .person__title {
    font-size: 13.5px; font-weight: 400; color: var(--text-muted);
    line-height: 22px;
  }

  .contact { position: absolute; right: 48px; top: 176px; }
  .contact__row {
    display: flex; align-items: center; justify-content: flex-end;
    gap: 12px; margin-bottom: 3px;
  }
  .contact__text {
    text-align: right; font-size: 11.5px; color: var(--text-dark);
    line-height: 14px;
  }
  .contact__icon { width: 13px; height: 14px; flex: none; }
  .contact__icon path, .contact__icon circle { fill: var(--icon); }
</style>
</head>
<body>
<div class="sheet">

  <div class="card card--front row-1">
    <div class="card__band"></div>
    <div class="card__frame"></div>
    <div class="brand-small">MixVault</div>
    <div class="person">
      <div class="person__name">DALLIN PERRY</div>
      <div class="person__title">ADR Mixer</div>
    </div>
    <div class="contact">
      <div class="contact__row">
        <div class="contact__text">248 - 5170 East Hollister<br>Vancouver, BC V5R 2J4</div>
        <svg class="contact__icon" viewBox="0 0 12 14"><path d="M6 0a5 5 0 0 0-5 5c0 3.6 5 9 5 9s5-5.4 5-9a5 5 0 0 0-5-5zm0 7a2 2 0 1 1 0-4 2 2 0 0 1 0 4z"/></svg>
      </div>
      <div class="contact__row">
        <div class="contact__text">604 518 2093</div>
        <svg class="contact__icon" viewBox="0 0 14 14"><path d="M3 0.5l2.2 2.8-1.3 1.6c.8 1.8 2.4 3.4 4.2 4.2l1.6-1.3 2.8 2.2-1.3 2.5C6 12.3 1.7 8 1.2 1.8z"/></svg>
      </div>
      <div class="contact__row">
        <div class="contact__text">www.MixVault.com</div>
        <svg class="contact__icon" viewBox="0 0 14 14"><path d="M7 0.5a6.5 6.5 0 1 0 0 13 6.5 6.5 0 0 0 0-13zm-1 2.2c.6.9.4 1.8-.4 2.2-.9.5-1 1.4-.2 2 .9.6.8 1.7.2 2.6-.4.6-.3 1.4.1 2A5 5 0 0 1 6 2.7zm3.5 1.1c.9.2 1.5 1 1.2 1.8-.3.7-1.2.8-1.7.3-.4-.5-.1-1.3.5-2.1z"/></svg>
      </div>
    </div>
  </div>

  <div class="card card--back row-1">
    <div class="card__frame"></div>
    <div class="brand-large">MixVault</div>
  </div>

  <div class="card card--front row-2">
    <div class="card__band"></div>
    <div class="card__frame"></div>
    <div class="brand-small">MixVault</div>
    <div class="person">
      <div class="person__name">REID CALLOWAY</div>
      <div class="person__title">Engineer / Director of Operations</div>
    </div>
    <div class="contact">
      <div class="contact__row">
        <div class="contact__text">248 - 5170 East Hollister<br>Vancouver, BC V5R 2J4</div>
        <svg class="contact__icon" viewBox="0 0 12 14"><path d="M6 0a5 5 0 0 0-5 5c0 3.6 5 9 5 9s5-5.4 5-9a5 5 0 0 0-5-5zm0 7a2 2 0 1 1 0-4 2 2 0 0 1 0 4z"/></svg>
      </div>
      <div class="contact__row">
        <div class="contact__text">604 518 2093</div>
        <svg class="contact__icon" viewBox="0 0 14 14"><path d="M3 0.5l2.2 2.8-1.3 1.6c.8 1.8 2.4 3.4 4.2 4.2l1.6-1.3 2.8 2.2-1.3 2.5C6 12.3 1.7 8 1.2 1.8z"/></svg>
      </div>
      <div class="contact__row">
        <div class="contact__text">www.MixVault.com</div>
        <svg class="contact__icon" viewBox="0 0 14 14"><path d="M7 0.5a6.5 6.5 0 1 0 0 13 6.5 6.5 0 0 0 0-13zm-1 2.2c.6.9.4 1.8-.4 2.2-.9.5-1 1.4-.2 2 .9.6.8 1.7.2 2.6-.4.6-.3 1.4.1 2A5 5 0 0 1 6 2.7zm3.5 1.1c.9.2 1.5 1 1.2 1.8-.3.7-1.2.8-1.7.3-.4-.5-.1-1.3.5-2.1z"/></svg>
      </div>
    </div>
  </div>

  <div class="card card--back row-2">
    <div class="card__frame"></div>
    <div class="brand-large">MixVault</div>
  </div>

</div>
</body>
</html>
```